Criação de Papelaria Profissional para Limpeza & Serviço para o lar
A empresa queria:
" Terceirizamos serviços de limpeza empresarial, portaria, recepção, copeira, limpeza pós-obra "

```html
<!DOCTYPE html>
<html lang="pt-BR">
<head>
<meta charset="utf-8">
<title>LarClaro — Papel Timbrado</title>
<link href="https://fonts.googleapis.com/css2?family=Roboto:wght@300;400;500;700&display=swap" rel="stylesheet">
<style>
  :root{
    --backdrop:#e9e7e4;
    --paper:#ffffff;
    --ink:#2b2b2b;
    --body-ink:#3a3a3a;
    --brand-blue:#2a6db5;
    --brand-green:#7cc242;
    --muted:#6d6d6d;
  }
  *{margin:0;padding:0;box-sizing:border-box}
  html,body{width:1200px;height:1200px;overflow:hidden;background:var(--backdrop);font-family:"Roboto",Arial,sans-serif}
  .letterhead{
    position:absolute;left:236px;top:24px;width:728px;height:1148px;
    background:var(--paper);box-shadow:0 6px 18px rgba(0,0,0,.18);overflow:hidden;
  }
  .brand{position:absolute;left:0;right:0;top:28px;display:flex;flex-direction:column;align-items:center;gap:12px}
  .brand-dot{width:72px;height:72px;border-radius:50%;background:var(--brand-green)}
  .brand-name{font-weight:700;font-size:40px;color:var(--brand-blue);letter-spacing:-.5px;line-height:1}
  .doc-title{position:absolute;left:74px;top:256px;font-weight:300;font-size:38px;color:var(--ink);letter-spacing:1px}
  .doc-body{position:absolute;left:74px;top:318px;width:580px;font-size:12px;line-height:19px;color:var(--body-ink);text-align:justify}
  .doc-body p{margin-bottom:18px}
  .doc-body p.lead{margin-bottom:38px}
  .doc-body p.second{margin-bottom:26px}
  .signature{position:absolute;left:0;right:0;top:890px;display:flex;flex-direction:column;align-items:center}
  .signature-mark{width:170px;height:80px;background:linear-gradient(180deg,#fff 0%,#d9d9d9 55%,#fff 100%);border-radius:6px}
  .signature-line{width:200px;height:1px;background:#555;margin-top:-2px}
  .signer-name{margin-top:6px;font-size:12px;font-weight:500;color:var(--ink)}
  .signer-role{font-size:11px;color:var(--brand-green);margin-top:2px}
  .contact-bar{position:absolute;left:36px;right:36px;top:1080px;display:flex;justify-content:space-between}
  .contact-item{display:flex;align-items:center;gap:6px;font-size:8.5px;line-height:12px;color:var(--muted)}
  .contact-item svg{width:16px;height:16px;flex:none}
  .bottom-band{position:absolute;left:0;right:0;bottom:0;height:24px;background:linear-gradient(90deg,var(--brand-blue),#4a90d9 50%,var(--brand-blue))}
</style>
</head>
<body>
<main class="letterhead">
  <header class="brand">
    <span class="brand-dot"></span>
    <span class="brand-name">LarClaro</span>
  </header>

  <h1 class="doc-title">TÍTULO</h1>

  <section class="doc-body">
    <p class="lead">Lorem Ipsum é simplesmente uma simulação de texto da indústria tipográfica e de impressos, e vem sendo utilizado desde o século XVI, quando um impressor desconhecido pegou uma bandeja de tipos e os embaralhou para fazer um livro de modelos de tipos. Lorem Ipsum sobreviveu não só a cinco séculos, como também ao salto para a editoração eletrônica, permanecendo essencialmente inalterado. Se popularizou na década de 60, quando a Tipofix lançou decalques contendo passagens de Lorem Ipsum, e mais recentemente quando passou a ser integrado a softwares de editoração eletrônica como Paginador Pro.</p>
    <p class="second">Lorem Ipsum é simplesmente uma simulação de texto da indústria tipográfica e de impressos, e vem sendo utilizado desde o século XVI, quando um impressor desconhecido pegou uma bandeja de tipos e os embaralhou para fazer um livro de modelos de tipos. Lorem Ipsum sobreviveu não só a cinco séculos, como também ao salto para a editoração eletrônica, permanecendo essencialmente inalterado. Se popularizou na década de 60, quan</p>
    <p>Lorem Ipsum é simplesmente uma simulação de texto da indústria tipográfica e de impressos, e vem sendo utilizado desde o século XVI, quando um impressor desconhecido pegou uma bandeja de tipos e os embaralhou para fazer</p>
    <p>Lorem Ipsum é simplesmente uma simulação de texto da indústria tipográfica e de impressos, e vem sendo utilizado desde o século XVI, quando um impressor desconhecido pegou uma bandeja de tipos e os embaralhou para fazer</p>
    <p>Lorem Ipsum é simplesmente uma simulação de texto da indústria tipográfica e de impressos, e vem sendo utilizado desde o século XVI, quando um impressor desconhecido pegou uma bandeja de tipos e os embaralhou para fazer</p>
    <p>Lorem Ipsum é simplesmente uma simulação de texto da indústria tipográfica e de impressos, e vem sendo utilizado desde o século XVI, quando um impressor desconhecido pegou uma bandeja de tipos e os embaralhou para fazer</p>
  </section>

  <section class="signature">
    <div class="signature-mark" role="img" aria-label="Assinatura manuscrita do responsável"></div>
    <div class="signature-line"></div>
    <div class="signer-name">Nome do Responsável</div>
    <div class="signer-role">Cargo</div>
  </section>

  <footer class="contact-bar">
    <div class="contact-item">
      <svg viewBox="0 0 16 16"><circle cx="8" cy="8" r="8" fill="#2a6db5"/><path d="M5.5 4.5l1.5-.3.8 2-1 .8a5 5 0 0 0 2.2 2.2l.8-1 2 .8-.3 1.5c-3.5.3-6.3-2.5-6-6z" fill="#fff"/></svg>
      <span>(00) 0000-0000<br>(00) 0000-0000</span>
    </div>
    <div class="contact-item">
      <svg viewBox="0 0 16 16"><circle cx="8" cy="8" r="8" fill="#2a6db5"/><rect x="4" y="5" width="8" height="6" rx="1" fill="#fff"/><path d="M4.3 5.4L8 8.3l3.7-2.9" stroke="#2a6db5" stroke-width=".8" fill="none"/></svg>
      <span>larclaro.com.br<br>contato@larclaro.com.br</span>
    </div>
    <div class="contact-item">
      <svg viewBox="0 0 16 16"><circle cx="8" cy="8" r="8" fill="#2a6db5"/><circle cx="8" cy="8" r="3.8" fill="none" stroke="#fff" stroke-width=".9"/><path d="M4.2 8h7.6M8 4.2c-1.6 2.2-1.6 5.4 0 7.6M8 4.2c1.6 2.2 1.6 5.4 0 7.6" stroke="#fff" stroke-width=".8" fill="none"/></svg>
      <span>www.larclaro.com.br<br>atendimento@larclaro.com.br</span>
    </div>
    <div class="contact-item">
      <svg viewBox="0 0 16 16"><circle cx="8" cy="8" r="8" fill="#2a6db5"/><path d="M8 3.5a3 3 0 0 1 3 3c0 2.2-3 5.8-3 5.8S5 8.7 5 6.5a3 3 0 0 1 3-3z" fill="#fff"/><circle cx="8" cy="6.5" r="1.1" fill="#2a6db5"/></svg>
      <span>Rua Exemplo, 000 - Bairro<br>Cidade - Estado - CEP 00000</span>
    </div>
  </footer>

  <div class="bottom-band"></div>
</main>
</body>
</html>
```